Eye catching Stationary Design

Healthcare consultant firm looking for stationary design ( letterhead, envelope and business cards) That’s professional, classy and eye catching . The design should incorporate the logo and the colors of the logo in its design. You can see the logo on our website at www crestmore advisory. net.

```html
<!DOCTYPE html>
<html lang="en">
<head>
<meta charset="utf-8">
<title>Crestmore Advisory – Envelope</title>
<link href="https://fonts.googleapis.com/css2?family=Roboto:wght@400;500&display=swap" rel="stylesheet">
<style>
  :root {
    --brand-blue: #004a98;
    --ink: #1f1f1f;
    --text-grey: #3a3a3a;
    --paper: #ffffff;
    --backdrop: #ecedef;
  }
  * { box-sizing: border-box; margin: 0; padding: 0; }
  html, body {
    width: 1200px; height: 800px; overflow: hidden;
    background: var(--backdrop);
    font-family: "Roboto", Arial, sans-serif;
  }
  .canvas {
    position: relative; width: 1200px; height: 800px;
  }
  .envelope {
    position: absolute; left: 240px; width: 720px; height: 360px;
    background: var(--paper);
    box-shadow: 0 2px 6px rgba(0,0,0,0.08);
    overflow: hidden;
  }
  .envelope--back { top: 24px; }
  .envelope--front { top: 416px; }
  .envelope__flap { position: absolute; top: 0; left: 0; width: 720px; height: 80px; }
  .brand {
    position: absolute; top: 40px; left: 44px;
    display: flex; align-items: center; gap: 10px;
  }
  .brand__mark {
    width: 22px; height: 22px; border-radius: 50%;
    background: var(--brand-blue);
  }
  .brand__name {
    font-size: 18px; font-weight: 500; color: var(--brand-blue);
    letter-spacing: 0.5px;
  }
  .contact {
    position: absolute; left: 40px; right: 40px; bottom: 34px;
    display: flex; align-items: center; gap: 12px;
    font-size: 10px; color: var(--text-grey); white-space: nowrap;
  }
  .contact__item { display: flex; align-items: center; gap: 4px; }
  .contact__icon { width: 10px; height: 10px; fill: var(--brand-blue); flex: none; }
  .envelope__band { position: absolute; left: 0; bottom: 0; width: 720px; height: 14px; }
</style>
</head>
<body>
<main class="canvas">
  <section class="envelope envelope--back" aria-label="Envelope back">
    <svg class="envelope__flap" viewBox="0 0 720 80" aria-hidden="true">
      <path d="M0 0 H720 V38 Q704 66 672 70 L640 74 H80 L48 70 Q16 66 0 38 Z" fill="var(--brand-blue)"/>
    </svg>
  </section>

  <section class="envelope envelope--front" aria-label="Envelope front">
    <div class="brand">
      <span class="brand__mark"></span>
      <span class="brand__name">Crestmore Advisory LLC</span>
    </div>

    <div class="contact">
      <span class="contact__item">118 Harlow Street, Brookfield, MA 01506, USA</span>
      <span class="contact__item">
        <svg class="contact__icon" viewBox="0 0 24 24" aria-hidden="true"><path d="M6.6 10.8a15.1 15.1 0 0 0 6.6 6.6l2.2-2.2a1 1 0 0 1 1-.25 11.4 11.4 0 0 0 3.6.57 1 1 0 0 1 1 1V20a1 1 0 0 1-1 1A17 17 0 0 1 3 4a1 1 0 0 1 1-1h3.5a1 1 0 0 1 1 1c0 1.25.2 2.45.57 3.57a1 1 0 0 1-.25 1z"/></svg>
        (555) 014-2290
      </span>
      <span class="contact__item">
        <svg class="contact__icon" viewBox="0 0 24 24" aria-hidden="true"><path d="M2 5h20v14H2z M4 7v.5l8 5.5 8-5.5V7l-8 5.5z" fill-rule="evenodd"/></svg>
        info@crestmoreadvisory.net
      </span>
      <span class="contact__item">
        <svg class="contact__icon" viewBox="0 0 24 24" aria-hidden="true"><circle cx="12" cy="12" r="10"/></svg>
        www.crestmoreadvisory.net
      </span>
    </div>

    <svg class="envelope__band" viewBox="0 0 720 14" preserveAspectRatio="none" aria-hidden="true">
      <polygon points="0,0 392,0 384,14 0,14" fill="var(--brand-blue)"/>
      <polygon points="396,6 720,6 720,14 390,14" fill="var(--ink)"/>
    </svg>
  </section>
</main>
</body>
</html>
```